New Card

Photography business
I want a sleek simple card that screams rich and classy. Black/Gold or silver font. No photos or images but would love a new logo When I hand someone my card I want compliments
Updates
My fiancé reminded me in 5 short months my name will change so I have changed my name to Colleen Abernathy
Also my BRAND is Lantern Field Photography, not my name. Thanks
Industry/Entity Type
Business
Contact Information for Business Card
Lantern Field Photography
Colleen Abernathy-owner
274 W. Hollis Ave.
Alder Point, NJ 08099
(856)555-0143
colleen@lanternfieldphotos.example
Look and feel
Each slider illustrates characteristics of the customer's brand and the style your logo design should communicate.

```html
<!DOCTYPE html>
<html lang="en">
<head>
<meta charset="utf-8">
<title>Lantern Field Photography – Business Cards</title>
<link href="https://fonts.googleapis.com/css2?family=Cinzel:wght@400&family=EB+Garamond:ital,wght@0,400;1,400&display=swap" rel="stylesheet">
<style>
  :root {
    --page: #ffffff;
    --card: #000000;
    --silver: #d2d2d2;
    --silver-soft: #bdbdbd;
    --ornament-dark: #3a3a3a;
    --ornament-light: #b8b8b8;
  }
  * { margin: 0; padding: 0; box-sizing: border-box; }
  html, body { width: 1200px; height: 794px; overflow: hidden; background: var(--page); }
  .sheet { position: relative; width: 1200px; height: 794px; }
  .card {
    position: absolute;
    width: 535px; height: 305px;
    background: var(--card);
    color: var(--silver);
    text-align: center;
    overflow: hidden;
  }
  .card--front { left: 28px; top: 82px; }
  .card--brand { left: 625px; top: 82px; }
  .card--plain { left: 28px; top: 413px; }
  .line { position: absolute; left: 0; right: 0; transform: translateY(-50%); white-space: nowrap; line-height: 1; }
  .name { font-family: "Cinzel", serif; font-size: 26px; letter-spacing: 0.3px; }
  .email { font-family: "EB Garamond", serif; font-style: italic; font-size: 19px; color: var(--silver-soft); }
  .address { font-family: "EB Garamond", serif; font-size: 19.5px; color: var(--silver-soft); }
  .phone { font-family: "EB Garamond", serif; font-size: 23px; }
  .brand-name { font-family: "Cinzel", serif; font-size: 26.5px; letter-spacing: 0.3px; }
  .website { font-family: "EB Garamond", serif; font-size: 20.5px; color: var(--silver-soft); }
  .flourish { position: absolute; left: 50px; width: 435px; }
  .flourish__rule { position: absolute; left: 0; right: 0; height: 1px; background: var(--silver-soft); }
  .flourish__ornament {
    position: absolute; left: 100px; width: 235px; height: 100%;
    background: radial-gradient(ellipse at center, var(--ornament-light) 0%, var(--ornament-dark) 60%, transparent 75%);
    opacity: 0.7;
  }
</style>
</head>
<body>
<main class="sheet">

  <section class="card card--front">
    <div class="flourish" style="top:44px;height:28px;">
      <div class="flourish__ornament" role="img" aria-label="Silver scrollwork ornament"></div>
      <div class="flourish__rule" style="top:26px;"></div>
    </div>
    <p class="line name" style="top:101px;">COLLEEN ABERNATHY</p>
    <p class="line email" style="top:132px;">colleen@lanternfieldphotos.example</p>
    <p class="line address" style="top:218px;">274 W. Hollis Ave. Alder Point, NJ 08099</p>
    <p class="line phone" style="top:247px;">856.555.0143</p>
  </section>

  <section class="card card--brand">
    <div class="flourish" style="top:94px;height:27px;">
      <div class="flourish__ornament" role="img" aria-label="Silver scrollwork ornament above the brand name"></div>
      <div class="flourish__rule" style="top:26px;"></div>
    </div>
    <p class="line brand-name" style="top:139px;">LANTERN FIELD PHOTOGRAPHY</p>
    <div class="flourish" style="top:157px;height:28px;">
      <div class="flourish__rule" style="top:1px;"></div>
      <div class="flourish__ornament" role="img" aria-label="Silver scrollwork ornament below the brand name"></div>
    </div>
    <p class="line website" style="top:251px;">www.lanternfieldphotos.example</p>
  </section>

  <section class="card card--plain">
    <p class="line name" style="top:120px;">COLLEEN ABERNATHY</p>
    <p class="line email" style="top:149px;">colleen@lanternfieldphotos.example</p>
    <p class="line address" style="top:220px;">274 W. Hollis Ave. Alder Point, NJ 08099</p>
    <p class="line phone" style="top:249px;">856.555.0143</p>
  </section>

</main>
</body>
</html>
```